Maplebright Savings Spree Promotional Postcard

I would like a postcard designed for a credit card balance transfer promotion.

The title for this promotion is "Maplebright savings spree".

(This paragraph should not be used word for word) Credit Card rates are on the rise since the Federal Prime Rate increase. I want to promote a non-variable rate credit card with rates as low as 7.9% APR* and free balance transfers. Simple, straightforward card with a low rate. There is no intro APR, always a great rate.

Below is some sample content options to highlight:
$0 Annual Fee
$0 Balance Transfer Fee
No Teaser, No Intro, just a great rate

Not only could you cut your interest rate in half, but you will also save hundreds of dollars by not paying any balance transfer fees.

Apply Today! www.tallowmerefin.org

Target Market(s)

Ages 25-45

Industry/Entity Type

Credit Card

Requirements
Must have
• Required disclaimer: *Annual Percentage Rate. 7.9% is the preferred rate based on qualifying credit. (teeny tiny disclaimer on front of card where rate is being advertised)
• Tagline: When you need OPTIONS ... (should be placed on back of postcard by credit union name, address, and logo)

```html
<!DOCTYPE html>
<html lang="en">
<head>
<meta charset="utf-8">
<title>Maplebright Savings Spree Postcard</title>
<link rel="stylesheet" href="https://fonts.googleapis.com/css2?family=Great+Vibes&family=Oswald:wght@500&family=Lato:ital,wght@1,300&family=Open+Sans:ital,wght@1,600&family=Quicksand:wght@600&display=swap">
<style>
  :root {
    --pink: #e0246a;
    --pink-deep: #c81d5c;
    --pink-soft: #f2b3cb;
    --charcoal: #333335;
    --white: #ffffff;
    --paper: #f3f3f3;
    --ink: #2a2a2a;
    --backdrop: #e9e6e3;
  }
  * { margin: 0; padding: 0; box-sizing: border-box; }
  html, body { width: 1200px; height: 825px; overflow: hidden; background: var(--backdrop); }
  .stage { position: relative; width: 1200px; height: 825px; }
  .postcard {
    position: absolute; left: 112px; top: 32px;
    width: 898px; height: 700px;
    transform: scale(1.086); transform-origin: 0 0;
    background: var(--paper); overflow: hidden;
    box-shadow: 0 6px 18px rgba(0,0,0,.18);
  }
  .postcard-shapes { position: absolute; inset: 0; }
  .photo { position: absolute; border-radius: 50%; }
  .photo-cupcake { left: 62px; top: 95px; width: 176px; height: 176px;
    background: radial-gradient(circle at 50% 60%, #c81d5c 0 28%, #f4eef0 30% 48%, #dfe3e6 70%); }
  .photo-rose { left: 344px; top: 167px; width: 122px; height: 122px;
    background: radial-gradient(circle at 50% 45%, #e88aa8 0 25%, #f5c9d7 40%, #e9dfe2 75%); }
  .brand { position: absolute; left: 490px; top: 110px; width: 360px; text-align: right;
    font-family: "Quicksand", sans-serif; color: var(--white); }
  .brand-name { font-size: 34px; font-weight: 600; line-height: 1; }
  .brand-sub { font-size: 18px; font-weight: 600; margin-top: 6px; }
  .headline { position: absolute; left: 70px; top: 350px;
    font-family: "Great Vibes", cursive; font-size: 56px; color: var(--pink); white-space: nowrap; }
  .benefits { position: absolute; left: 0; top: 435px; list-style: none; }
  .benefit { height: 44px; margin-bottom: 11px; padding-left: 44px;
    border: 2.5px solid var(--pink); border-left: none; border-radius: 0 24px 24px 0;
    font-family: "Open Sans", sans-serif; font-style: italic; font-weight: 600;
    font-size: 22px; line-height: 39px; color: var(--ink); background: var(--white); }
  .benefit-fee { width: 253px; }
  .benefit-transfer { width: 372px; }
  .benefit-rate { width: 518px; }
  .options { position: absolute; left: 578px; top: 310px; width: 292px; color: var(--white); }
  .options-title { font-family: "Oswald", sans-serif; font-weight: 500; font-size: 27px; letter-spacing: .3px; text-align: right; }
  .options-script { font-family: "Great Vibes", cursive; font-size: 34px; color: var(--pink); text-align: right; margin-top: 2px; }
  .options-copy { font-family: "Lato", sans-serif; font-style: italic; font-weight: 300;
    font-size: 16.5px; line-height: 24px; text-align: right; margin-top: 4px; }
  .rate { position: absolute; left: 585px; top: 521px; width: 330px; height: 42px;
    border: 2.5px solid var(--pink); border-radius: 22px;
    font-family: "Oswald", sans-serif; font-weight: 500; font-size: 20px; line-height: 37px;
    color: var(--white); padding-left: 16px; }
  .cta { position: absolute; left: 0; right: 0; top: 645px; text-align: center;
    font-family: "Quicksand", sans-serif; font-weight: 600; font-size: 23px;
    letter-spacing: 4px; color: var(--white); }
</style>
</head>
<body>
<main class="stage">
  <article class="postcard">
    <svg class="postcard-shapes" viewBox="0 0 898 700" width="898" height="700" aria-hidden="true">
      <path d="M0 0H898V225C760 215 560 190 420 205C260 222 120 250 0 265Z" fill="var(--pink)"/>
      <path d="M0 265C120 250 260 222 420 205C560 190 760 215 898 225V245C760 232 560 210 420 224C260 240 120 268 0 282Z" fill="var(--white)"/>
      <path d="M898 225V238C760 226 620 222 556 226" fill="none" stroke="var(--pink-deep)" stroke-width="3"/>
      <path d="M556 230C640 222 780 226 898 240V628H620C580 628 556 604 556 566Z" fill="var(--charcoal)"/>
      <path d="M0 610C250 630 600 630 898 605V700H0Z" fill="var(--pink)"/>
      <path d="M0 600C250 622 600 622 898 596V605C600 630 250 630 0 610Z" fill="#d9d9d9"/>
      <circle cx="150" cy="183" r="104" fill="var(--pink-soft)"/>
      <circle cx="405" cy="228" r="80" fill="var(--pink-soft)"/>
    </svg>
    <div class="photo photo-cupcake" role="img" aria-label="Photo of a cupcake with white frosting topped by a red paper heart"></div>
    <div class="photo photo-rose" role="img" aria-label="Photo of pink frosted cupcakes with a sugar rose"></div>
    <header class="brand">
      <div class="brand-name">Tallowmere Financial</div>
      <div class="brand-sub">credit union</div>
    </header>
    <h1 class="headline">Maplebright savings spree</h1>
    <ul class="benefits">
      <li class="benefit benefit-fee">$0 Annual Fee</li>
      <li class="benefit benefit-transfer">$0 Balance Transfer Fee</li>
      <li class="benefit benefit-rate">No Teaser, No Intro, just a great rate</li>
    </ul>
    <section class="options">
      <h2 class="options-title">WHEN YOU NEED OPTIONS</h2>
      <p class="options-script">We are here for you</p>
      <p class="options-copy">Not only could you cut your interest rate in half, but you will also save hundreds of dollars by not paying any balance transfer fees.</p>
    </section>
    <p class="rate">ANNUAL PERCENTAGE RATE. 7.9%</p>
    <footer class="cta">Apply Today! www.tallowmerefin.org</footer>
  </article>
</main>
</body>
</html>
```